I would love for my business card to be fun and sophisicated. The clients are people that could afford nice well crafted wigs. These wigs are not like granny wigs. The're for women who are stylish and what to look there best especially if they are dealing with cancer are some from of hair loss. Do not want the card to appear crowded with to much information. If I need to eliminate some data, let me know.
Thanks

Industry/Entity Type

Hair

Contact Information for Business Card

L Radiant Tresses, Marjorie Ellison, owner, stylist

Wigs/Studio Showroom
Extensions
Hair Replacement
Private Room

24683 Mesa Vista Loop, Suite. R
Irvine, CA 90871
(949) 555-0178
Email: tresses@lradianttresses-example.com
www.lradianttresses-example.com

```html
<!DOCTYPE html>
<html lang="en">
<head>
<meta charset="utf-8">
<title>L Radiant Tresses – Business Card</title>
<link href="https://fonts.googleapis.com/css2?family=Questrial&display=swap" rel="stylesheet">
<style>
  :root {
    --backdrop: #d9d9d9;
    --backdrop-edge: #a9a9a9;
    --brand-red: #e3262c;
    --ink: #1d1d1d;
    --ink-soft: #555555;
    --rule: #6b6b6b;
    --card-white: #ffffff;
    --blush-light: #f6c4c4;
    --blush-mid: #e89a9e;
    --mauve-deep: #7b5566;
    --band-tint: rgba(255, 255, 255, 0.28);
  }
  * { margin: 0; padding: 0; box-sizing: border-box; }
  html, body {
    width: 1200px; height: 900px; overflow: hidden;
  }
  body {
    background: radial-gradient(ellipse at 50% 45%, var(--backdrop) 0%, var(--backdrop-edge) 100%);
    font-family: "Questrial", "Century Gothic", sans-serif;
    position: relative;
  }
  .card {
    position: absolute;
    width: 580px; height: 332px;
    border-radius: 3px;
    overflow: hidden;
    box-shadow: 0 14px 30px rgba(0, 0, 0, 0.28);
  }

  /* Front */
  .card--front { left: 310px; top: 70px; }
  .front-backdrop {
    position: absolute; inset: 0;
    background:
      radial-gradient(circle at 20% 30%, rgba(255,255,255,0.35) 0 8%, transparent 20%),
      radial-gradient(circle at 75% 25%, rgba(255,255,255,0.3) 0 6%, transparent 18%),
      radial-gradient(circle at 85% 65%, rgba(255,255,255,0.25) 0 7%, transparent 18%),
      linear-gradient(170deg, var(--blush-light) 0%, var(--blush-mid) 50%, var(--mauve-deep) 100%);
  }
  .front-brand {
    position: absolute; left: 0; right: 0; top: 112px;
    text-align: center;
    color: var(--brand-red);
    font-size: 44px;
    letter-spacing: 1px;
  }
  .front-band {
    position: absolute; left: 0; right: 0; top: 236px; height: 52px;
    background: var(--band-tint);
    border-top: 1px solid rgba(255,255,255,0.45);
    border-bottom: 1px solid rgba(255,255,255,0.45);
    display: flex; align-items: center; justify-content: center;
  }
  .front-web {
    color: var(--card-white);
    font-size: 19px;
    letter-spacing: 2.5px;
  }

  /* Back */
  .card--back { left: 310px; top: 482px; background: var(--card-white); }
  .back-brand {
    position: absolute; right: 36px; top: 34px;
    color: var(--brand-red);
    font-size: 32px;
    letter-spacing: 0.5px;
  }
  .back-details {
    position: absolute; left: 190px; right: 36px; top: 100px;
  }
  .holder-name {
    color: var(--brand-red);
    font-size: 25px;
    letter-spacing: 3px;
    text-transform: uppercase;
    line-height: 1;
  }
  .holder-role {
    color: var(--ink);
    font-size: 12px;
    letter-spacing: 3px;
    text-transform: uppercase;
    margin-top: 4px;
  }
  .contact-list {
    list-style: none;
    margin-top: 10px;
    padding-bottom: 8px;
    border-bottom: 2px dotted var(--rule);
  }
  .contact-item {
    display: flex; align-items: center; gap: 10px;
    font-size: 15px; color: var(--ink);
    line-height: 24px;
  }
  .contact-icon { width: 16px; height: 16px; flex: none; }
  .address {
    font-style: normal;
    color: var(--ink-soft);
    font-size: 17px;
    line-height: 24px;
    margin-top: 10px;
  }
</style>
</head>
<body>

  <section class="card card--front" aria-label="Card front">
    <div class="front-backdrop" role="img" aria-label="Soft pink bokeh light background"></div>
    <div class="front-brand">L Radiant Tresses</div>
    <div class="front-band"><span class="front-web">www.lradianttresses-example.com</span></div>
  </section>

  <section class="card card--back" aria-label="Card back">
    <div class="back-brand">L Radiant Tresses</div>
    <div class="back-details">
      <div class="holder-name">Marjorie Ellison</div>
      <div class="holder-role">Owner,</div>
      <ul class="contact-list">
        <li class="contact-item">
          <svg class="contact-icon" viewBox="0 0 16 16" aria-hidden="true"><path d="M3.5 1.5l2.5 3-1.5 1.5c.8 1.8 2.2 3.2 4 4l1.5-1.5 3 2.5-1.5 2.5C7 13 3 9 1 3.5z" fill="var(--brand-red)"/></svg>
          <span>: (949) 555-0178</span>
        </li>
        <li class="contact-item">
          <svg class="contact-icon" viewBox="0 0 16 16" aria-hidden="true"><rect x="1" y="3" width="14" height="10" fill="none" stroke="var(--brand-red)" stroke-width="1.4"/><path d="M1 3l7 6 7-6" fill="none" stroke="var(--brand-red)" stroke-width="1.4"/></svg>
          <span>: tresses@lradianttresses-example.com</span>
        </li>
        <li class="contact-item">
          <svg class="contact-icon" viewBox="0 0 16 16" aria-hidden="true"><circle cx="8" cy="8" r="6.5" fill="none" stroke="var(--brand-red)" stroke-width="1.4"/><ellipse cx="8" cy="8" rx="2.8" ry="6.5" fill="none" stroke="var(--brand-red)" stroke-width="1.2"/><path d="M1.5 8h13" stroke="var(--brand-red)" stroke-width="1.2"/></svg>
          <span>: www.lradianttresses-example.com</span>
        </li>
      </ul>
      <address class="address">24683 Mesa Vista Loop, Suite. R<br>Irvine, CA 90871</address>
    </div>
  </section>

</body>
</html>
```